Postcard double sided

Title: DWIGHT'S REVENGE

Why would Dwight Kessler align himself with Gordon Pruett?

(photo of two guys)

Dwight approached elected officials that he wanted to run for office, but did not have money to finance his campaign. He wanted other elected officials to finance his campaign. Everyone told him that they would help him get the vote out, but that he needed to finance his own race.

In comes Gordon Pruett.

Gordon Pruett who has a pay to play scheme over at the City, told Dwight he would finance his campaign on one condition.

He needed to run against Steven Hulse.

Why would Dwight want to run with no money?

Backside

DWIGHT'S REVENGE

Dwight decided to run because no one on the school board would terminate Dwight's ex and her new boyfriend who both work for the school district. His ex even filed criminal charges against him that are still pending.

Mug Shot facing left (name the charges Criminal Trespass , and Criminal Mischief (highlight bold letters use two lines) mug shot facing right

Complaint one (then photo with full face) Compliant 2)
(showcharges)

Dwight's ultimate goal is to terminate his ex and her new boyfriend if elected.
Plus Gordon Pruett needs the majority on the school board to do what he does bet.

Kickbacks for Contracts.

They will hire their own contractors!
Say "No" to Dwight's Revenge and Gordon Pruett Money Grab!

Title On Back: all caps: DOMESTIC VIOLENCE

```html
<!DOCTYPE html>
<html lang="en">
<head>
<meta charset="utf-8">
<title>Dwight's Revenge – Postcard</title>
<link href="https://fonts.googleapis.com/css2?family=Tinos:wght@400;700&family=PT+Sans:wght@400;700&display=swap" rel="stylesheet">
<style>
  :root{
    --navy:#1f2a5e;
    --navy-deep:#172049;
    --red:#c1202e;
    --title-red:#e2202f;
    --pill-navy:#242f6b;
    --white:#ffffff;
    --body-text:#e9ecf5;
    --page:#ececec;
    --serif:"Tinos", "Times New Roman", serif;
    --sans:"PT Sans", Arial, sans-serif;
  }
  *{box-sizing:border-box;margin:0;padding:0}
  html,body{width:1029px;height:1200px;overflow:hidden;background:var(--page)}
  .canvas{position:relative;width:1029px;height:1200px}

  .postcard{
    position:absolute;left:64px;width:700px;height:400px;
    transform:scale(1.2857);transform-origin:top left;
    background:var(--white);box-shadow:0 3px 10px rgba(0,0,0,.25);overflow:hidden;
  }
  .postcard--front{top:50px}
  .postcard--back{top:636px}

  .panel{position:absolute;left:0;top:0;width:350px;height:400px;color:var(--white)}
  .panel-bg{position:absolute;inset:0;width:350px;height:400px}
  .panel > *:not(.panel-bg){position:absolute}

  .title{left:0;width:350px;text-align:center;font-family:var(--serif);font-weight:700;font-size:30px;letter-spacing:.5px;line-height:1}
  .title .accent{color:var(--title-red)}
  .rule{left:78px;width:194px;height:1px;background:linear-gradient(90deg,transparent,rgba(255,255,255,.85),transparent)}

  .subtitle{left:20px;width:310px;text-align:center;font-family:var(--serif);font-size:17px;line-height:20px}
  .body-copy{left:26px;width:310px;font-family:var(--sans);font-size:10px;line-height:12.6px;text-align:justify;color:var(--body-text)}
  .lead-in{left:0;width:350px;text-align:center;font-family:var(--serif);font-size:14px;color:var(--title-red)}
  .question{left:0;width:350px;text-align:center;font-family:var(--serif);font-size:14px}

  .pill{border-radius:11px;text-align:center;color:var(--white);line-height:20px}
  .pill--navy{left:54px;width:232px;height:20px;background:var(--pill-navy);font-family:var(--serif);font-size:12px;box-shadow:0 1px 3px rgba(0,0,0,.35)}
  .pill--red{left:26px;width:308px;height:21px;background:var(--red);font-family:var(--sans);font-weight:700;font-size:10px;line-height:21px;box-shadow:0 1px 3px rgba(0,0,0,.4)}

  .photo-area{position:absolute;left:350px;top:0;width:350px;height:400px;
    background:linear-gradient(180deg,#2b3f78 0%,#223466 55%,#141a2c 100%)}

  .frame{background:var(--white);padding:4px;box-shadow:0 2px 4px rgba(0,0,0,.35)}
  .frame .shot{width:100%;height:100%;background:linear-gradient(180deg,#8a8e94,#5f6a63)}
  .frame .doc{width:100%;height:100%;background:linear-gradient(180deg,#f4f4f4,#dcdcdc)}
  .mug-profile-left{left:26px;top:144px;width:71px;height:84px}
  .mug-profile-right{left:105px;top:144px;width:71px;height:84px}
  .mug-front{left:188px;top:144px;width:96px;height:120px}
  .complaint-one{left:291px;top:144px;width:46px;height:57px;padding:2px}
  .complaint-two{left:291px;top:206px;width:46px;height:57px;padding:2px}

  .charge{width:71px;text-align:center;font-family:var(--sans);font-weight:700;font-size:9px;line-height:11px;top:238px}
  .charge--trespass{left:26px}
  .charge--mischief{left:105px}

  .tagline{left:0;width:350px;text-align:center;font-family:var(--serif);font-size:11.5px}
</style>
</head>
<body>
<main class="canvas">

  <!-- Front -->
  <section class="postcard postcard--front">
    <div class="panel">
      <svg class="panel-bg" viewBox="0 0 350 400" preserveAspectRatio="none" aria-hidden="true">
        <defs>
          <linearGradient id="navyFront" x1="0" y1="0" x2="1" y2="1">
            <stop offset="0" stop-color="#25316a"/><stop offset="1" stop-color="#1a2452"/>
          </linearGradient>
        </defs>
        <rect width="350" height="400" fill="url(#navyFront)"/>
        <polygon points="0,241 175,262 350,241 350,254 175,279 0,254" fill="#ffffff"/>
        <polygon points="0,254 175,279 350,254 350,400 0,400" fill="#c1202e"/>
      </svg>

      <h1 class="title" style="top:31px">DWIGHT'S <span class="accent">REVENGE</span></h1>
      <div class="rule" style="top:73px"></div>
      <h2 class="subtitle" style="top:91px">Why would Dwight Kessler align himself with Gordon Pruett?</h2>
      <p class="body-copy" style="top:144px">Dwight approached elected officials that he wanted to run for office, but did not have money to finance his campaign. He wanted other elected officials to finance his campaign. Everyone told him that they would help him get the vote out, but that he needed to finance his own race.</p>
      <p class="lead-in" style="top:226px">In comes Gordon Pruett.</p>
      <p class="body-copy" style="top:292px">Gordon Pruett who has a pay to play scheme over at the City, told Dwight he would finance his campaign on one condition.</p>
      <p class="pill pill--navy" style="top:336px">He needed to run against Steven Hulse.</p>
      <p class="question" style="top:366px">Why would Dwight want to run with no money?</p>
    </div>
    <div class="photo-area" role="img" aria-label="Photo of Dwight Kessler and Gordon Pruett standing together in suits in front of a blue campaign backdrop"></div>
  </section>

  <!-- Back -->
  <section class="postcard postcard--back">
    <div class="panel">
      <svg class="panel-bg" viewBox="0 0 350 400" preserveAspectRatio="none" aria-hidden="true">
        <defs>
          <linearGradient id="navyBack" x1="0" y1="0" x2="1" y2="1">
            <stop offset="0" stop-color="#25316a"/><stop offset="1" stop-color="#1a2452"/>
          </linearGradient>
        </defs>
        <rect width="350" height="400" fill="url(#navyBack)"/>
        <polygon points="0,133 350,133 350,268 175,280 0,268" fill="#c1202e"/>
        <polygon points="0,268 175,280 350,268 350,274 175,286 0,274" fill="#ffffff"/>
      </svg>

      <h1 class="title" style="top:19px">DOMESTIC <span class="accent">VIOLENCE</span></h1>
      <div class="rule" style="top:57px"></div>
      <p class="body-copy" style="top:67px">Dwight decided to run because no one on the school board would terminate Dwight's ex and her new boyfriend who both work for the school district. His ex even filed criminal charges against him that are still pending.</p>

      <div class="frame mug-profile-left"><div class="shot" role="img" aria-label="Booking photo, profile facing left"></div></div>
      <div class="frame mug-profile-right"><div class="shot" role="img" aria-label="Booking photo, profile facing right"></div></div>
      <div class="frame mug-front"><div class="shot" role="img" aria-label="Booking photo, front view"></div></div>
      <div class="frame complaint-one"><div class="doc" role="img" aria-label="Criminal complaint document one"></div></div>
      <div class="frame complaint-two"><div class="doc" role="img" aria-label="Criminal complaint document two"></div></div>

      <p class="charge charge--trespass">CRIMINAL<br>TRESPASS</p>
      <p class="charge charge--mischief">CRIMINAL<br>MISCHIEF</p>

      <p class="body-copy" style="top:293px;text-align:left">Dwight's ultimate goal is to terminate his ex and her new boyfriend if elected. Plus Gordon Pruett needs the majority on the school board to do what he does bet.</p>
      <p class="tagline" style="top:343px">Kickbacks for Contracts. They will hire their own contractors!</p>
      <p class="pill pill--red" style="top:367px">Say "No" to Dwight's Revenge and Gordon Pruett Money Grab!</p>
    </div>
  </section>

</main>
</body>
</html>
```